Graphic to show our studio's values

We'd like to create a graphic of our values that can go onto fun gifts for our team in order to keep our values in front of all of us in a creative way. The graphic might go onto mugs, gift boxes, tote bags, etc. We are a growing interior architecture/design studio in Austin, TX. I encourage you to check out our website at www.morvankestudio.com to get a sense of our vibe and culture. The graphic may or may not include the subtext to each value depending on how difficult it is to incorporate the subtext into a great design.

```html
<!DOCTYPE html>
<html lang="en">
<head>
<meta charset="utf-8">
<title>Morvanke Studio — Our Values</title>
<link rel="stylesheet" href="https://fonts.googleapis.com/css2?family=Barlow+Semi+Condensed:wght@600;700&display=swap">
<style>
  :root {
    --green: #8dc63f;
    --charcoal: #4a4b4d;
    --slate: #636466;
    --outline: #a7a9ac;
    --paper: #ffffff;
  }
  html, body {
    margin: 0;
    padding: 0;
    width: 1200px;
    height: 1200px;
    overflow: hidden;
    background: var(--paper);
  }
  .canvas {
    position: relative;
    width: 1200px;
    height: 1200px;
    background: var(--paper);
    font-family: "Barlow Semi Condensed", "Arial Narrow", sans-serif;
  }
  .brand {
    position: absolute;
    top: 196px;
    left: 0;
    width: 1200px;
    text-align: center;
    font-weight: 600;
    font-size: 46px;
    line-height: 1;
    letter-spacing: 0;
    color: var(--charcoal);
  }
  .values-wheel {
    position: absolute;
    top: 0;
    left: 0;
    width: 1200px;
    height: 1200px;
  }
  .ring-guide { fill: none; stroke: var(--outline); stroke-width: 1.5; }
  .segment, .segment-head { stroke: var(--paper); stroke-width: 4; stroke-linejoin: round; }
  .is-green { fill: var(--green); }
  .is-dark { fill: var(--charcoal); }
  .value-label {
    font-family: "Barlow Semi Condensed", "Arial Narrow", sans-serif;
    font-weight: 600;
    font-size: 31px;
    letter-spacing: 1.5px;
    fill: var(--paper);
  }
  .wheel-title {
    font-family: "Barlow Semi Condensed", "Arial Narrow", sans-serif;
    font-weight: 700;
    font-size: 60px;
    letter-spacing: 1px;
  }
  .title-our { fill: var(--slate); }
  .title-values { fill: var(--green); }
  .badge-ring { fill: var(--paper); stroke: var(--outline); stroke-width: 1.5; }
  .badge-icon { fill: var(--paper); }
  .badge-line { fill: none; stroke: var(--paper); stroke-linecap: round; stroke-linejoin: round; }
</style>
</head>
<body>
<div class="canvas">

  <header class="brand">Morvanke Studio</header>

  <svg class="values-wheel" viewBox="0 0 1200 1200" xmlns="http://www.w3.org/2000/svg">
    <defs>
      <path id="segment-body" d="M263.2 697.2 A337 337 0 0 1 588.2 372.2 L590.5 436.2 A273 273 0 0 0 327.2 699.5 Z"/>
      <polygon id="segment-arrow" points="587.4,349.2 653.0,408.6 591.3,459.2"/>
      <path id="label-path-learners" d="M305.2 698.7 A295 295 0 0 1 589.7 414.2"/>
      <path id="label-path-positive" d="M610.3 414.2 A295 295 0 0 1 894.8 698.7"/>
      <path id="label-path-trustworthy" d="M611.0 1023.8 A315 315 0 0 0 914.8 720.0"/>
      <path id="label-path-responsive" d="M285.2 720.0 A315 315 0 0 0 589.0 1023.8"/>
    </defs>

    <circle class="ring-guide" cx="600" cy="709" r="343"/>
    <circle class="ring-guide" cx="600" cy="709" r="267"/>

    <g class="ring-segments">
      <use href="#segment-body" class="segment is-green"/>
      <use href="#segment-body" class="segment is-dark" transform="rotate(90 600 709)"/>
      <use href="#segment-body" class="segment is-green" transform="rotate(180 600 709)"/>
      <use href="#segment-body" class="segment is-dark" transform="rotate(270 600 709)"/>
    </g>
    <g class="ring-arrows">
      <use href="#segment-arrow" class="segment-head is-green"/>
      <use href="#segment-arrow" class="segment-head is-dark" transform="rotate(90 600 709)"/>
      <use href="#segment-arrow" class="segment-head is-green" transform="rotate(180 600 709)"/>
      <use href="#segment-arrow" class="segment-head is-dark" transform="rotate(270 600 709)"/>
    </g>

    <text class="value-label"><textPath href="#label-path-learners" startOffset="50%" text-anchor="middle">WE ARE LEARNERS</textPath></text>
    <text class="value-label"><textPath href="#label-path-positive" startOffset="50%" text-anchor="middle">WE ARE POSITIVE</textPath></text>
    <text class="value-label"><textPath href="#label-path-trustworthy" startOffset="50%" text-anchor="middle">WE ARE TRUSTWORTHY</textPath></text>
    <text class="value-label"><textPath href="#label-path-responsive" startOffset="50%" text-anchor="middle">WE ARE RESPONSIVE</textPath></text>

    <text class="wheel-title" x="600" y="730" text-anchor="middle"><tspan class="title-our">OUR </tspan><tspan class="title-values">VALUES</tspan></text>

    <g class="badge badge-learners">
      <circle class="badge-ring" cx="489" cy="576" r="46"/>
      <circle class="is-dark" cx="489" cy="576" r="39"/>
      <circle class="badge-icon" cx="489" cy="561" r="10"/>
      <path class="badge-icon" d="M471 592 Q471 574 489 574 Q507 574 507 592 Z"/>
      <rect class="badge-icon" x="466" y="594" width="46" height="5" rx="1.5"/>
    </g>

    <g class="badge badge-positive">
      <circle class="badge-ring" cx="726" cy="576" r="46"/>
      <circle class="is-green" cx="726" cy="576" r="39"/>
      <rect class="badge-icon" x="705" y="572" width="9" height="22" rx="1.5"/>
      <path class="badge-icon" d="M717 572 L727 559 Q729 551 734 553 Q738 556 735 566 L745 566 Q750 567 749 573 L745 590 Q743 594 738 594 L717 594 Z"/>
    </g>

    <g class="badge badge-responsive">
      <circle class="badge-ring" cx="489" cy="819" r="46"/>
      <circle class="is-green" cx="489" cy="819" r="39"/>
      <circle cx="489" cy="819" r="20" fill="none" stroke="var(--paper)" stroke-width="8" stroke-dasharray="7.85 7.85"/>
      <circle class="badge-icon" cx="489" cy="819" r="16"/>
      <circle class="is-green" cx="489" cy="819" r="7"/>
    </g>

    <g class="badge badge-trustworthy">
      <circle class="badge-ring" cx="726" cy="819" r="46"/>
      <circle class="is-dark" cx="726" cy="819" r="39"/>
      <path class="badge-line" d="M726 797 L744 804 L744 818 Q744 834 726 842 Q708 834 708 818 L708 804 Z" stroke-width="3.5"/>
      <path class="badge-line" d="M717 819 L724 826 L736 812" stroke-width="4"/>
    </g>
  </svg>

</div>
</body>
</html>
```